QRV Consulting Web Design… We need a Facelift!

We currently have a website but it is very outdated. We like our content, but could use some help on giving it a refreshed facelift.

www.QRV-Consulting.example is our site

We only consult with large companies in the US that have sales over $250,000 a year, so looking to be high end yet approachable in our look.

Target Market(s)

Large corporations

Industry/Entity Type

Consulting

Coding

Coded - Design and coding required

Number of Pages Required

5+ page

Font styles to use
Serif
Sans Serif

Requirements
Must have
• We love our logo, keep that the same.
• The site colors can deviate from the logo, as long as it is complimentary
Nice to have
• We like our videos and graphics. If you can make them better, then great! But you can also feel free to reuse them.
• There is a video on the opening screen and one on the video page.
• We would like the video on the video page to be incorporated on the first page.
• If you think we need other/more page, we are all ears!
Should not have
• Want to set us apart from our competition in look, feel, professionalism and step away from the old fashioned conservatives of their websites. We want to be professional, yet bolder and fresher.
• Our Competition is LedgerPilot.example and TheBrindlewoodGroup.example, but not looking to copy of emulate them, but gives an idea of the world QRV is in.

```html
<!DOCTYPE html>
<html lang="en">
<head>
<meta charset="utf-8">
<title>QRV Consulting – Treasury Pricing</title>
<link href="https://fonts.googleapis.com/css2?family=Open+Sans:wght@400;600;700&family=Raleway:wght@400;600;700&display=swap" rel="stylesheet">
<style>
:root{
  --red:#d23a3f;
  --blue:#3f7fc0;
  --navy:#1f2b3a;
  --ink:#4a4f55;
  --muted:#8a9097;
  --line:#e2e4e7;
  --panel:#f1f2f4;
  --footer:#26292d;
  --footer-bar:#1b1d20;
  --white:#ffffff;
}
*{box-sizing:border-box;margin:0;padding:0}
html,body{width:1200px;height:3076px;overflow:hidden}
body{font-family:"Open Sans",Arial,sans-serif;color:var(--ink);background:var(--white);font-size:13px;line-height:1.55}
h1,h2,h3,h4{font-family:"Raleway","Open Sans",sans-serif;font-weight:600}
section{overflow:hidden}

/* header */
.site-header{height:112px;display:flex;align-items:center;justify-content:space-between;padding:0 60px;border-bottom:1px solid var(--line)}
.brand{display:flex;align-items:center;gap:12px}
.brand-dot{width:34px;height:34px;border-radius:50%;background:var(--red)}
.brand-name{font-size:22px;font-weight:700;color:var(--navy)}
.main-nav{display:flex;gap:34px;align-items:center;font-size:14px}
.main-nav a{color:var(--ink);text-decoration:none}
.main-nav a.active{color:var(--red);font-weight:600}

/* hero */
.hero{position:relative;height:588px}
.hero-photo{position:absolute;inset:0;background:linear-gradient(180deg,#9aa6b3 0%,#c9ced4 45%,#eef0f2 78%,#ffffff 100%)}
.hero-copy{position:absolute;top:150px;left:0;right:0;text-align:center}
.hero-title{font-size:40px;color:var(--white);letter-spacing:.5px;text-shadow:0 2px 6px rgba(0,0,0,.25)}
.hero-sub{font-size:28px;color:var(--red);font-weight:600;font-family:"Raleway",sans-serif;margin-top:6px}
.btn{display:inline-block;font-size:12px;font-weight:600;letter-spacing:1px;padding:10px 22px;text-transform:uppercase}
.btn-red{background:var(--red);color:var(--white);margin-top:22px}
.hero-features{position:absolute;bottom:30px;left:0;right:0;display:flex;justify-content:center;gap:120px}
.feature{width:220px;text-align:center;font-size:15px;color:var(--navy)}
.feature-photo{width:100px;height:100px;border-radius:50%;margin:0 auto 14px;border:5px solid var(--white);box-shadow:0 2px 8px rgba(0,0,0,.2);background:linear-gradient(135deg,#8fa2b6,#d7dde3)}
.hero-rule{position:absolute;bottom:0;left:0;right:0;height:6px;background:linear-gradient(90deg,var(--red) 0 50%,var(--blue) 50% 100%)}

/* video */
.intro{height:350px;display:flex;align-items:center;padding:0 100px;gap:80px}
.video-frame{position:relative;width:420px;height:300px;flex:none;background:linear-gradient(135deg,#e8eef5,#c9d8ea)}
.play{position:absolute;left:50%;top:50%;width:60px;height:60px;margin:-30px 0 0 -30px;border-radius:50%;background:var(--red);display:flex;align-items:center;justify-content:center}
.intro-copy{flex:1}
.intro-copy h2{font-size:30px;color:var(--blue);font-weight:400;line-height:1.25}
.intro-copy h2 strong{color:var(--red);font-weight:600}
.intro-copy p{margin:18px 0 22px;font-size:13px}
.btn-outline{border:1px solid #bfc3c8;color:var(--ink);background:var(--white)}

/* section headings */
.section-title{text-align:center;font-size:34px;font-weight:400;color:var(--blue);line-height:1.3}
.section-title span{color:var(--red)}

/* unique */
.unique{height:500px;background:var(--panel);padding-top:60px}
.unique-grid{display:grid;grid-template-columns:repeat(4,1fr);gap:20px;padding:0 100px;margin-top:40px}
.unique-photo{height:180px;background:linear-gradient(135deg,#b7c3cf,#e4e8ec)}
.unique-label{height:32px;line-height:32px;color:var(--white);font-size:13px;font-weight:600;padding-left:12px}
.label-red{background:var(--red)}
.label-blue{background:var(--blue)}
.unique-card p{font-size:12px;padding:12px 4px 0;color:var(--muted)}

/* process */
.process{height:460px;padding-top:50px}
.process-grid{display:flex;justify-content:center;gap:100px;margin-top:36px}
.process-card{width:200px;height:300px;border:1px solid var(--line);box-shadow:0 2px 6px rgba(0,0,0,.06);text-align:center;padding-top:22px;background:var(--white)}
.ring{width:96px;height:96px;margin:0 auto;border-radius:50%;border:10px solid var(--red);border-right-color:#e5e7ea;display:flex;align-items:center;justify-content:center}
.process-card h3{font-size:17px;color:var(--blue);margin:14px 0 10px}
.process-card ul{list-style:none;text-align:left;padding:0 18px 0 22px;font-size:11px;line-height:1.5}
.process-card li{padding-left:14px;position:relative;margin-bottom:5px}
.process-card li::before{content:"";position:absolute;left:0;top:6px;width:5px;height:5px;border-radius:50%;background:var(--red)}

/* why */
.why{height:430px;background:var(--panel);padding-top:56px}
.why-grid{display:grid;grid-template-columns:repeat(5,1fr);gap:26px;padding:0 100px;margin-top:36px;text-align:center}
.why-icon{width:110px;height:110px;margin:0 auto;border-radius:50%;background:var(--white);border:6px solid var(--red);box-shadow:inset 0 0 0 6px #f6d9da;display:flex;align-items:center;justify-content:center}
.why-item h4{font-size:16px;color:var(--red);margin:14px 0 8px}
.why-item p{font-size:11.5px;color:var(--muted);text-align:justify}

/* testimonials */
.testimonials{height:330px;padding-top:50px}
.quote-row{display:flex;justify-content:center;gap:70px;margin-top:36px}
.quote{display:flex;gap:24px;width:420px}
.avatar{flex:none;width:100px;height:100px;border-radius:50%;background:linear-gradient(135deg,#9fb0c2,#dfe5eb)}
.quote p{font-size:12px;color:var(--muted)}
.quote h4{font-size:15px;color:var(--red);margin-top:8px}
.quote small{font-size:11px;color:var(--muted)}
.pager{display:flex;justify-content:center;gap:12px;margin-top:26px}
.pager span{width:32px;height:32px;border-radius:50%;background:#d8dadd;display:flex;align-items:center;justify-content:center}

/* footer */
.site-footer{height:270px;background:var(--footer);color:#b8bcc1;padding:50px 100px 0;display:grid;grid-template-columns:1.2fr .8fr 1.1fr 1.1fr;gap:40px;font-size:12px}
.site-footer h4{color:var(--white);font-size:15px;margin-bottom:14px}
.site-footer ul{list-style:none}
.site-footer li{margin-bottom:5px}
.social{display:flex;gap:8px;margin-top:16px}
.social span{width:26px;height:26px;border-radius:50%;background:#4a4f56}
.contact-line{display:flex;gap:10px;margin-bottom:10px;align-items:flex-start}
.contact-line svg{flex:none;margin-top:3px}
.signup{display:flex;margin-top:14px}
.signup span{flex:1;height:32px;background:#3a3e44}
.signup b{width:80px;height:32px;background:var(--blue);color:var(--white);font-size:11px;display:flex;align-items:center;justify-content:center}
.footer-bar{height:36px;background:var(--footer-bar);color:#8b9096;font-size:11px;display:flex;align-items:center;justify-content:center}
</style>
</head>
<body>

<header class="site-header">
  <div class="brand"><span class="brand-dot"></span><span class="brand-name">QRV Consulting</span></div>
  <nav class="main-nav">
    <a class="active" href="#">Why QRV?</a>
    <a href="#">Our Process</a>
    <a href="#">Contact Us</a>
    <a href="#">About Us</a>
    <a href="#">Client List</a>
    <svg width="16" height="16" viewBox="0 0 16 16"><circle cx="6.5" cy="6.5" r="5" fill="none" stroke="#4a4f55" stroke-width="2"/><line x1="10" y1="10" x2="15" y2="15" stroke="#4a4f55" stroke-width="2"/></svg>
  </nav>
</header>

<section class="hero">
  <div class="hero-photo" role="img" aria-label="Photo of two business professionals reviewing documents in an office"></div>
  <div class="hero-copy">
    <h1 class="hero-title">TAKING YOUR TREASURY PRICING PROCESS</h1>
    <div class="hero-sub">To unprecedented levels</div>
    <span class="btn btn-red">Negotiating Fee Tips</span>
  </div>
  <div class="hero-features">
    <div class="feature"><div class="feature-photo" role="img" aria-label="Photo of a chart on a desk"></div>Comparative analysis modeling</div>
    <div class="feature"><div class="feature-photo" role="img" aria-label="Photo of colleagues shaking hands"></div>Relationship profitability modeling</div>
    <div class="feature"><div class="feature-photo" role="img" aria-label="Photo of financial documents"></div>Treasury analysis</div>
  </div>
  <div class="hero-rule"></div>
</section>

<section class="intro">
  <div class="video-frame" role="img" aria-label="Video still showing a treasury cash management cycle graphic and a presenter">
    <span class="play"><svg width="22" height="22" viewBox="0 0 22 22"><path d="M6 3l13 8-13 8z" fill="#fff"/></svg></span>
  </div>
  <div class="intro-copy">
    <h2>Taking Your Treasury <strong>Pricing</strong><br>process</h2>
    <p>QRV Consulting works closely with your team assisting in auditing your bank fees and earnings credit rates. As former bankers, we bring our industry and regional bank experience to the table to supplement your team in providing insider knowledge to review bank pricing and services. Whether you need fresh pricing, data, and terms, we help ensure you manage your treasury with confidence.</p>
    <span class="btn btn-outline">View More</span>
  </div>
</section>

<section class="unique">
  <h2 class="section-title">What Makes <span>us Unique</span></h2>
  <div class="unique-grid">
    <div class="unique-card"><div class="unique-photo" role="img" aria-label="Photo of a team meeting around a table"></div><div class="unique-label label-red">Know The Market</div><p>Focusing on your business – not on banking. Ever-increasing information gap in knowledge is difficult to keep up with changes.</p></div>
    <div class="unique-card"><div class="unique-photo" role="img" aria-label="Photo of a consultant at a laptop"></div><div class="unique-label label-blue">Understand Profitability</div><p>Pricing is determined by profitability over time, say other firms. QRV consulting provides a smarter way to review relationships.</p></div>
    <div class="unique-card"><div class="unique-photo" role="img" aria-label="Photo of a handshake between partners"></div><div class="unique-label label-red">Improve Your Team</div><p>Focusing on your business – not on banking. Ever-increasing information gap in knowledge is difficult to keep up with changes.</p></div>
    <div class="unique-card"><div class="unique-photo" role="img" aria-label="Photo of a monitor showing financial charts"></div><div class="unique-label label-blue">Work Best Practices</div><p>Focusing on your business – not on banking. Ever-increasing information gap in knowledge is difficult to keep up with changes.</p></div>
  </div>
</section>

<section class="process">
  <h2 class="section-title">Our <span>Process</span></h2>
  <div class="process-grid">
    <div class="process-card">
      <div class="ring"><svg width="34" height="34" viewBox="0 0 34 34"><rect x="4" y="18" width="6" height="12" fill="#3f7fc0"/><rect x="14" y="10" width="6" height="20" fill="#3f7fc0"/><rect x="24" y="4" width="6" height="26" fill="#3f7fc0"/></svg></div>
      <h3>Model</h3>
      <ul><li>Build option models</li><li>Model analysis against</li><li>Build calculate profitability</li></ul>
    </div>
    <div class="process-card">
      <div class="ring"><svg width="34" height="34" viewBox="0 0 34 34"><circle cx="12" cy="12" r="5" fill="#3f7fc0"/><circle cx="23" cy="12" r="5" fill="#3f7fc0"/><path d="M3 28c0-6 4-9 9-9s9 3 9 9zM15 28c0-6 4-9 9-9s8 3 8 9z" fill="#3f7fc0"/></svg></div>
      <h3>Engage</h3>
      <ul><li>Review relevant strategies</li><li>Discuss with providers</li><li>Finalize agreements</li></ul>
    </div>
    <div class="process-card">
      <div class="ring"><svg width="34" height="34" viewBox="0 0 34 34"><path d="M6 18l8 8 15-17" fill="none" stroke="#3f7fc0" stroke-width="4"/></svg></div>
      <h3>Audit</h3>
      <ul><li>Ongoing pricing adherence</li><li>Continue market benchmarking</li><li>Complete contract compliance</li></ul>
    </div>
  </div>
</section>

<section class="why">
  <h2 class="section-title">Why <span>QRV?</span></h2>
  <div class="why-grid">
    <div class="why-item"><div class="why-icon"><svg width="44" height="44" viewBox="0 0 44 44"><path d="M4 36l12-12 8 8 16-18" fill="none" stroke="#d23a3f" stroke-width="4"/></svg></div><h4>Profitability</h4><p>Clients enjoy gains they never thought possible by looking beyond market pricing and improving every fee line.</p></div>
    <div class="why-item"><div class="why-icon"><svg width="44" height="44" viewBox="0 0 44 44"><path d="M22 4L4 14h36zM8 17h5v17H8zM19.5 17h5v17h-5zM31 17h5v17h-5zM4 37h36v4H4z" fill="#d23a3f"/></svg></div><h4>Insiders</h4><p>Our team has managed treasury personnel as well as client relationships from within banks.</p></div>
    <div class="why-item"><div class="why-icon"><svg width="44" height="44" viewBox="0 0 44 44"><circle cx="22" cy="14" r="8" fill="#d23a3f"/><path d="M6 40c0-10 7-15 16-15s16 5 16 15z" fill="#d23a3f"/></svg></div><h4>Involved</h4><p>Clients enjoy gains we provide before with millions of dollars in annualized savings on their accounts.</p></div>
    <div class="why-item"><div class="why-icon"><svg width="44" height="44" viewBox="0 0 44 44"><circle cx="19" cy="19" r="12" fill="none" stroke="#d23a3f" stroke-width="4"/><line x1="28" y1="28" x2="40" y2="40" stroke="#d23a3f" stroke-width="5"/></svg></div><h4>Thorough</h4><p>A complete line-by-line review. We do the work, you make the decisions.</p></div>
    <div class="why-item"><div class="why-icon"><svg width="44" height="44" viewBox="0 0 44 44"><ellipse cx="22" cy="10" rx="14" ry="5" fill="#d23a3f"/><path d="M8 14v8c0 3 6 5 14 5s14-2 14-5v-8c0 3-6 5-14 5S8 17 8 14zM8 26v8c0 3 6 5 14 5s14-2 14-5v-8c0 3-6 5-14 5S8 29 8 26z" fill="#d23a3f"/></svg></div><h4>Data</h4><p>Fee Compass™ is our proprietary, intuitive tool that systematically examines and analyzes treasury pricing and terms.</p></div>
  </div>
</section>

<section class="testimonials">
  <h2 class="section-title">Client <span>Testimonials</span></h2>
  <div class="quote-row">
    <div class="quote"><div class="avatar" role="img" aria-label="Portrait photo of a client"></div><div><p>"In the 20 years I've been in treasury management, I really feel their knowledge and experience made a real difference in our bank pricing review."</p><h4>Treasurer of a National Retailer</h4><small>Retail Company</small></div></div>
    <div class="quote"><div class="avatar" role="img" aria-label="Portrait photo of a client"></div><div><p>"The last thing we need to do is upset the existing relationships we have with our banks. Employing a mutually beneficial approach in negotiating was perfect."</p><h4>CFO of a National Healthcare</h4><small>Company</small></div></div>
  </div>
  <div class="pager">
    <span><svg width="12" height="12" viewBox="0 0 12 12"><path d="M8 1L3 6l5 5" fill="none" stroke="#fff" stroke-width="2"/></svg></span>
    <span><svg width="12" height="12" viewBox="0 0 12 12"><path d="M4 1l5 5-5 5" fill="none" stroke="#fff" stroke-width="2"/></svg></span>
  </div>
</section>

<footer class="site-footer">
  <div>
    <h4>QRV Consultings</h4>
    <p>QRV Consulting works closely with your team assisting in auditing your bank fees and earnings credit rates.</p>
    <div class="social"><span></span><span></span><span></span><span></span></div>
  </div>
  <div>
    <h4>Why QRV?</h4>
    <ul><li>› Profitability</li><li>› Insiders</li><li>› Involved</li><li>› Thorough</li><li>› Data</li></ul>
  </div>
  <div>
    <h4>Contact us</h4>
    <div class="contact-line"><svg width="12" height="14" viewBox="0 0 12 14"><path d="M6 0a5 5 0 0 0-5 5c0 4 5 9 5 9s5-5 5-9a5 5 0 0 0-5-5z" fill="#d23a3f"/></svg><span>210 Harbor Line Road, Suite 4, Fairview, OH 40000</span></div>
    <div class="contact-line"><svg width="12" height="12" viewBox="0 0 12 12"><path d="M2 0h3l1 3-2 1a7 7 0 0 0 4 4l1-2 3 1v3a1 1 0 0 1-1 1A11 11 0 0 1 1 1a1 1 0 0 1 1-1z" fill="#d23a3f"/></svg><span>(555) 014-2270</span></div>
    <div class="contact-line"><svg width="12" height="10" viewBox="0 0 12 10"><rect width="12" height="10" fill="#d23a3f"/><path d="M0 0l6 5 6-5" fill="none" stroke="#26292d"/></svg><span>hello@qrv-consulting.example</span></div>
  </div>
  <div>
    <h4>Sign up for newsletter</h4>
    <p>Newsletter and insight updates sent direct to your inbox.</p>
    <div class="signup"><span></span><b>Sign Up</b></div>
  </div>
</footer>
<div class="footer-bar">© 2016 QRV Consulting. All Rights Reserved.</div>

</body>
</html>
```